Firm Stationery Design

I need a design for stationery, including: Stationery First Page, Stationery Second Sheet, Envelope, Mailing Label for Flat Envelopes, and Business Cards

```html
<!DOCTYPE html>
<html lang="en">
<head>
<meta charset="utf-8">
<title>Harlow Law LLC – Envelope</title>
<link href="https://fonts.googleapis.com/css2?family=Montserrat:wght@400;800&display=swap" rel="stylesheet">
<style>
  :root {
    --backdrop: #3b3b3b;
    --paper: #f7f7f5;
    --ink: #101010;
    --accent: #f29a17;
    --muted: #2a2a2a;
  }
  * { box-sizing: border-box; margin: 0; padding: 0; }
  html, body {
    width: 1200px;
    height: 800px;
    overflow: hidden;
    background: var(--backdrop);
    font-family: "Montserrat", sans-serif;
  }
  .canvas {
    position: relative;
    width: 1200px;
    height: 800px;
  }
  .envelope {
    position: absolute;
    left: 250px;
    width: 700px;
    height: 350px;
    background: var(--paper);
    overflow: hidden;
  }
  .envelope--front { top: 35px; }
  .envelope--back { top: 415px; }

  /* Front */
  .brand {
    position: absolute;
    top: 40px;
    left: 44px;
    display: flex;
    align-items: center;
    gap: 10px;
  }
  .brand__square {
    width: 20px;
    height: 20px;
    background: var(--accent);
  }
  .brand__name {
    font-weight: 800;
    font-size: 18px;
    letter-spacing: 0.5px;
    color: var(--ink);
  }
  .return-address {
    position: absolute;
    left: 44px;
    bottom: 44px;
    font-size: 13px;
    line-height: 1.35;
    color: var(--muted);
  }
  .colour-bands {
    position: absolute;
    top: 0;
    right: 0;
    width: 360px;
    height: 100%;
  }
  .colour-bands .band--ink { fill: var(--ink); }
  .colour-bands .band--paper { fill: var(--paper); }
  .colour-bands .band--accent { fill: var(--accent); }

  /* Back */
  .flap {
    position: absolute;
    top: 0;
    left: 0;
    width: 100%;
    height: 170px;
    background: var(--ink);
    border-radius: 0 0 36px 36px;
    display: flex;
    align-items: center;
    justify-content: center;
  }
  .flap__name {
    font-weight: 800;
    font-size: 26px;
    letter-spacing: 1px;
    color: var(--paper);
  }
</style>
</head>
<body>
  <main class="canvas">
    <section class="envelope envelope--front">
      <div class="brand">
        <span class="brand__square"></span>
        <span class="brand__name">HARLOW LAW LLC</span>
      </div>
      <p class="return-address">Your address, City<br>State, Zip 1234</p>
      <svg class="colour-bands" viewBox="0 0 360 350" aria-hidden="true">
        <polygon class="band--ink" points="90,0 240,0 170,350 0,350"/>
        <polygon class="band--paper" points="240,0 275,0 205,350 170,350"/>
        <polygon class="band--accent" points="275,0 360,0 360,40 298,350 205,350"/>
      </svg>
    </section>

    <section class="envelope envelope--back">
      <div class="flap">
        <span class="flap__name">HARLOW LAW LLC</span>
      </div>
    </section>
  </main>
</body>
</html>
```